Small boutique multi-family apartment developer needs premium website design.

We are a growing real estate development company specializing in multi family apartment development. Our company Brindel Asset Development focuses on passive real estate investors looking to maximize their current real estate portfolio by allowing us to develop and reposition their current properties allowing them more cashflow while we are also able to take over the management of their asset in order to ensure optimal performance on a consistent basis.

```html
<!DOCTYPE html>
<html lang="en">
<head>
<meta charset="utf-8">
<title>Brindel Asset Development</title>
<link href="https://fonts.googleapis.com/css2?family=Poppins:wght@300;400;500;600;700;800&display=swap" rel="stylesheet">
<style>
:root{
  --green:#3fc89b;
  --green-dark:#2fb487;
  --ink:#1d1d1f;
  --muted:#7b7b7b;
  --mint:#eef9f5;
  --white:#ffffff;
}
*{margin:0;padding:0;box-sizing:border-box}
html,body{width:1200px;height:3637px;overflow:hidden}
body{font-family:'Poppins',sans-serif;color:var(--ink);background:var(--white);position:relative}
.abs{position:absolute}
.accent{color:var(--green)}
.btn{position:absolute;display:flex;align-items:center;justify-content:center;background:var(--green);color:var(--white);border-radius:24px;font-size:13px;font-weight:600;text-transform:uppercase}
.section-title{position:absolute;left:0;width:1200px;text-align:center;font-size:36px;font-weight:700;text-transform:uppercase;letter-spacing:.3px}
.section-lead{position:absolute;text-align:center;font-size:14.5px;color:var(--muted);line-height:22px;font-weight:300}
.photo{position:absolute}

/* header */
.site-header{position:absolute;left:0;top:0;width:1200px;height:86px;background:var(--white)}
.brand{position:absolute;left:88px;top:31px;font-size:15px;font-weight:600;color:var(--green);white-space:nowrap;line-height:22px}
.main-nav{position:absolute;top:34px;left:337px;display:flex;gap:40px;font-size:11.5px;letter-spacing:.8px;color:#444}
.search-btn{position:absolute;left:1063px;top:28px;width:26px;height:26px;border-radius:50%;background:var(--green)}

/* hero */
.hero{position:absolute;left:0;top:86px;width:1200px;height:542px;background:linear-gradient(90deg,#7a6d62 0%,#a89a8e 35%,#d9d4cc 60%,#c8c2ba 100%)}
.hero h1{position:absolute;left:88px;top:128px;font-size:51px;line-height:55px;font-weight:800;color:var(--white);text-transform:uppercase}
.hero-sub{position:absolute;left:88px;top:296px;font-size:22px;font-weight:600;color:var(--white)}
.hero-text{position:absolute;left:88px;top:334px;font-size:14px;line-height:22px;color:var(--white);font-weight:300}
.hero-dots{position:absolute;left:89px;top:477px;display:flex;gap:5px}
.hero-dots span{width:9px;height:9px;border-radius:50%;background:var(--white)}
.hero-dots span.on{background:var(--green)}
.social-rail{position:absolute;left:30px;top:104px;width:24px}
.social-rail .dot{width:8px;height:8px;border-radius:50%;background:var(--white);margin:0 auto 19px}
.social-rail .ring{width:24px;height:24px;border-radius:50%;border:1.5px solid var(--green);margin-bottom:14px;position:relative}
.social-rail .ring::after{content:"";position:absolute;left:8px;top:8px;width:6px;height:6px;border-radius:50%;background:var(--white)}
.scroll-label{position:absolute;left:36px;top:384px;transform:rotate(-90deg);transform-origin:left top;font-size:9.5px;letter-spacing:1.5px;color:var(--white);font-weight:600;white-space:nowrap}

/* about */
.about-title{position:absolute;left:668px;top:758px;font-size:34px;font-weight:700}
.about-text{position:absolute;left:668px;top:826px;width:350px;font-size:14px;line-height:22.2px;color:var(--muted);font-weight:300}

/* process */
.process{position:absolute;left:0;top:1197px;width:1200px;height:583px;background:var(--mint)}
.process-card{position:absolute;top:201px;width:214px;height:215px;background:var(--white);text-align:center}
.process-card.active{box-shadow:0 6px 16px rgba(0,0,0,.06)}
.process-card.active::after{content:"";position:absolute;left:0;bottom:-7px;width:100%;height:7px;background:var(--green)}
.process-card svg{position:absolute;left:62px;top:18px}
.process-card h3{position:absolute;top:88px;width:100%;font-size:17px;font-weight:700;text-transform:uppercase}
.process-card p{position:absolute;top:118px;left:20px;width:174px;font-size:14px;line-height:22px;color:var(--muted);font-weight:300}
.nav-arrow{position:absolute;top:312px;width:30px;height:30px;border-radius:50%;border:1.5px solid var(--green);background:var(--white)}

/* services */
.services{position:absolute;left:0;top:1780px;width:1200px;height:591px;background:linear-gradient(100deg,#6d6356 0%,#a49480 40%,#b7a68e 60%,#8e8374 100%)}
.services-disc{position:absolute;left:142px;top:62px;width:472px;height:472px;border-radius:50%;background:var(--white);text-align:center}
.services-disc h2{margin-top:86px;font-size:35px;font-weight:700;text-transform:uppercase}
.services-disc h3{margin-top:12px;font-size:17px;font-weight:700;text-transform:uppercase}
.services-disc p{margin:10px auto 0;width:370px;font-size:14px;line-height:22px;color:var(--muted);font-weight:300}
.services-link{display:inline-block;margin-top:14px;font-size:13px;font-weight:600;border-bottom:1.5px solid var(--ink)}

/* footer */
.site-footer{position:absolute;left:0;top:3225px;width:1200px;height:412px;background:var(--green);color:var(--white)}
.footer-brand{position:absolute;left:99px;top:180px;font-size:16px;font-weight:600;white-space:nowrap;line-height:22px}
.footer-col h4{font-size:18px;font-weight:500;text-transform:uppercase}
.footer-col ul{list-style:none;margin-top:20px}
.footer-col li{font-size:12.5px;line-height:27px}
.footer-col li::before{content:"› ";font-weight:600}
.contact-item{position:absolute;left:0;font-size:12.5px;line-height:18px;padding-left:23px}
.contact-item svg{position:absolute;left:0;top:2px}
.newsletter-input{position:absolute;left:0;top:98px;width:258px;height:46px;border-radius:24px;background:var(--white);color:#666;font-size:12.5px;padding:13px 0 0 38px}
.to-top{position:absolute;left:1112px;top:337px;width:40px;height:40px;border-radius:50%;background:var(--white)}
.copyright{position:absolute;left:0;top:380px;width:1200px;text-align:center;font-size:12px;font-weight:600}
</style>
</head>
<body>

<header class="site-header">
  <div class="brand">Brindel Asset Development</div>
  <nav class="main-nav"><span>HOME</span><span>ABOUT US</span><span>SERVICES</span><span>OUR PROCESS</span><span>PORTFOLIO</span><span>PROJECTS</span><span>CONTACT US</span></nav>
  <div class="search-btn"><svg width="26" height="26" viewBox="0 0 26 26"><circle cx="12" cy="12" r="4.5" fill="none" stroke="#fff" stroke-width="1.8"/><line x1="15.3" y1="15.3" x2="18" y2="18" stroke="#fff" stroke-width="1.8"/></svg></div>
</header>

<section class="hero">
  <div class="photo" role="img" aria-label="Two business professionals reviewing documents at a laptop" style="inset:0"></div>
  <div class="social-rail">
    <div class="ring"></div><div class="dot"></div><div class="dot"></div><div class="dot"></div>
    <div style="width:1.5px;height:56px;background:#fff;margin:0 auto"></div>
  </div>
  <div class="scroll-label">SCROLL DOWN</div>
  <svg class="abs" style="left:32px;top:398px" width="22" height="26" viewBox="0 0 22 26"><circle cx="11" cy="11" r="10" fill="#3fc89b"/><path d="M11 8v14M7 18l4 4 4-4" stroke="#fff" stroke-width="1.4" fill="none"/></svg>
  <h1>Maximizing<br>Your Real Estate<br>Portfolio With</h1>
  <div class="hero-sub">Expert Development and Management</div>
  <div class="hero-text">Specializing in multi-family apartment development, we<br>help investors enhance their properties for greater returns."</div>
  <div class="btn" style="left:89px;top:394px;width:193px;height:43px">Get Started Now</div>
  <div class="hero-dots"><span></span><span class="on"></span><span></span><span></span><span></span></div>
</section>

<section>
  <div class="photo" role="img" aria-label="Two colleagues reviewing a tablet" style="left:184px;top:719px;width:207px;height:179px;background:linear-gradient(160deg,#c9d2da,#3b4250)"></div>
  <div class="photo" role="img" aria-label="Business handshake across a table" style="left:401px;top:719px;width:207px;height:179px;background:linear-gradient(160deg,#d7e2ee,#2e3a52)"></div>
  <div class="photo" role="img" aria-label="Two businessmen discussing papers in a bright office" style="left:184px;top:908px;width:424px;height:207px;background:linear-gradient(100deg,#e8e8e6,#9ea3aa 50%,#d9d7d2)"></div>
  <h2 class="about-title">ABOUT <span class="accent">US</span></h2>
  <p class="about-text">At Brindel Asset Development, we partner with passive real estate investors to maximize the potential of their properties. Our team specializes in multi-family apartment development, repositioning, and management to deliver consistent performance and increased cash flow for our clients.</p>
  <div class="btn" style="left:668px;top:1002px;width:140px;height:44px">Read More</div>
</section>

<section class="process">
  <h2 class="section-title" style="top:61px"><span class="accent">OUR</span> PROCESS</h2>
  <p class="section-lead" style="left:260px;top:116px;width:680px">Step-by-Step Process: Briefly outline how Brindel Asset Development works with investors from initial consultation to development and ongoing management.</p>
  <div class="nav-arrow" style="left:106px"><svg width="27" height="27" viewBox="0 0 27 27"><path d="M15 10l-3.5 3.5L15 17" stroke="#333" stroke-width="1.5" fill="none"/></svg></div>
  <div class="nav-arrow" style="left:1062px"><svg width="27" height="27" viewBox="0 0 27 27"><path d="M12 10l3.5 3.5L12 17" stroke="#333" stroke-width="1.5" fill="none"/></svg></div>

  <div class="process-card" style="left:158px">
    <svg width="90" height="66" viewBox="0 0 90 66"><circle cx="30" cy="30" r="29" fill="#cfeee2"/><rect x="36" y="8" width="22" height="14" rx="3" fill="none" stroke="#222" stroke-width="2"/><circle cx="30" cy="30" r="5" fill="none" stroke="#222" stroke-width="2"/><circle cx="54" cy="30" r="5" fill="none" stroke="#222" stroke-width="2"/><path d="M20 52v-8a8 8 0 0 1 16 0v8M44 52v-8a8 8 0 0 1 16 0v8M22 52h40" stroke="#222" stroke-width="2" fill="none"/></svg>
    <h3>Consultation</h3><p>We start by understanding your investment goals</p>
  </div>
  <div class="process-card active" style="left:383px">
    <svg width="90" height="66" viewBox="0 0 90 66"><circle cx="30" cy="30" r="29" fill="#cfeee2"/><rect x="28" y="18" width="28" height="26" rx="2" fill="none" stroke="#222" stroke-width="2"/><path d="M34 38v-6M40 38v-10M46 38v-14" stroke="#222" stroke-width="2"/><circle cx="58" cy="44" r="7" fill="none" stroke="#3fc89b" stroke-width="2"/><line x1="63" y1="49" x2="68" y2="54" stroke="#222" stroke-width="2"/></svg>
    <h3>Strategy</h3><p>Develop a custom plan to maximize your property's potential</p>
  </div>
  <div class="process-card" style="left:607px">
    <svg width="90" height="66" viewBox="0 0 90 66"><circle cx="30" cy="30" r="29" fill="#cfeee2"/><path d="M26 38l10-10 8 6 14-14M52 20h6v6" stroke="#222" stroke-width="2" fill="none"/><circle cx="42" cy="50" r="7" fill="none" stroke="#222" stroke-width="2"/><path d="M28 58h30" stroke="#222" stroke-width="2"/></svg>
    <h3>Developmen</h3><p>Expert execution to reposition and enhance your property</p>
  </div>
  <div class="process-card" style="left:826px">
    <svg width="90" height="66" viewBox="0 0 90 66"><circle cx="30" cy="30" r="29" fill="#cfeee2"/><path d="M32 52v-6a14 14 0 1 1 14 0v6z" fill="none" stroke="#222" stroke-width="2"/><circle cx="54" cy="22" r="7" fill="none" stroke="#3fc89b" stroke-width="2"/><path d="M34 56h10" stroke="#222" stroke-width="2"/></svg>
    <h3>Management</h3><p>Ongoing asset management for long-term success</p>
  </div>
  <div class="btn" style="left:504px;top:469px;width:192px;height:42px">View Our Portfolio</div>
</section>

<section class="services">
  <div class="photo" role="img" aria-label="Architectural scale model of a high-rise apartment tower" style="inset:0;background:linear-gradient(100deg,rgba(0,0,0,0) 55%,rgba(150,80,55,.45) 70%,rgba(0,0,0,0) 90%)"></div>
  <div class="services-disc">
    <h2><span class="accent">OUR</span> SERVICES</h2>
    <h3>Development and Repositioning</h3>
    <p>Our expertise in multi-family apartment development allows us to transform your existing properties into modern, high-performing assets. Whether through new construction or repositioning, we help you increase property value and cash flow."</p>
    <span class="services-link">Explore Our Services &gt;</span>
    <svg style="display:block;margin:20px auto 0" width="94" height="44" viewBox="0 0 94 44"><circle cx="22" cy="22" r="21" fill="#111"/><path d="M31 22H13M19 16l-6 6 6 6" stroke="#fff" stroke-width="2" fill="none"/><circle cx="72" cy="22" r="21" fill="#3fc89b"/><path d="M63 22h18M75 16l6 6-6 6" stroke="#fff" stroke-width="2" fill="none"/></svg>
  </div>
</section>

<section>
  <h2 class="section-title" style="top:2455px"><span class="accent">OUR</span> PROJECTS</h2>
  <p class="section-lead" style="left:215px;top:2517px;width:770px">At Brindel Asset Development, we excel in transforming multi-family properties to achieve optimal performance and enhanced returns for our investors. Our approach combines strategic development and repositioning with expert management to maximize cash flow and property value.</p>
  <div class="photo" role="img" aria-label="Modern house exterior with glass balcony and garden" style="left:160px;top:2620px;width:211px;height:431px;background:linear-gradient(180deg,#e4eaec,#9b8a72 55%,#8ea06a)"></div>
  <div class="photo" role="img" aria-label="House construction model on blueprints" style="left:377px;top:2620px;width:216px;height:212px;background:linear-gradient(150deg,#c7b08e,#6d6e72)"></div>
  <div class="photo" role="img" aria-label="Modern stone and wood house at dusk" style="left:600px;top:2620px;width:215px;height:212px;background:linear-gradient(160deg,#3c4a63,#8d6c4e)"></div>
  <div class="photo" role="img" aria-label="Classic dining room with large windows" style="left:823px;top:2620px;width:215px;height:212px;background:linear-gradient(160deg,#d8c29a,#8d6d47)"></div>
  <div class="photo" role="img" aria-label="Cutaway 3D floor plan of an apartment" style="left:377px;top:2839px;width:216px;height:212px;background:linear-gradient(160deg,#e9e4da,#7fa55b)"></div>
  <div class="photo" role="img" aria-label="Living room with tall black-framed windows" style="left:600px;top:2839px;width:215px;height:212px;background:linear-gradient(180deg,#5d6a5a,#e8e4dc)"></div>
  <div class="photo" role="img" aria-label="Bright living room with white sofas and stone wall" style="left:823px;top:2839px;width:215px;height:212px;background:linear-gradient(160deg,#cfc8be,#f0eeea)"></div>
  <div class="btn" style="left:504px;top:3092px;width:192px;height:42px">View Our Projects</div>
</section>

<footer class="site-footer">
  <div class="footer-brand">Brindel Asset Development</div>
  <div class="footer-col abs" style="left:361px;top:70px">
    <h4>Quick Links</h4>
    <ul><li>Home</li><li>About Us</li><li>Services</li><li>Our Process</li><li>Portfolio</li><li>Projects</li><li>Contact Us</li></ul>
  </div>
  <div class="footer-col abs" style="left:546px;top:70px;width:220px;height:220px">
    <h4>Contact Info</h4>
    <div class="contact-item" style="top:46px"><svg width="13" height="11" viewBox="0 0 13 11"><rect width="13" height="10" rx="1" fill="#fff"/><path d="M0 1l6.5 5L13 1" stroke="#3fc89b" fill="none"/></svg>Email:<br>info@brindelasset.com</div>
    <div class="contact-item" style="top:100px"><svg width="13" height="13" viewBox="0 0 13 13"><path d="M2 1l3 1 1 3-2 1a8 8 0 0 0 3 3l1-2 3 1 1 3c-6 1-11-4-10-10z" fill="#fff"/></svg>Phone:<br>+08 555 014 2290</div>
    <div class="contact-item" style="top:154px"><svg width="11" height="14" viewBox="0 0 11 14"><path d="M5.5 0a5.5 5.5 0 0 1 5.5 5.5C11 9 5.5 14 5.5 14S0 9 0 5.5A5.5 5.5 0 0 1 5.5 0z" fill="#fff"/><circle cx="5.5" cy="5.5" r="2" fill="#3fc89b"/></svg>Location:<br>Brindel Asset</div>
  </div>
  <div class="footer-col abs" style="left:795px;top:72px;width:260px">
    <h4>Newsletter</h4>
    <p style="font-size:12.5px;line-height:18px;margin-top:20px">Subscribe to our email address to get the latest news.</p>
    <div class="newsletter-input">Enter your email...
      <svg class="abs" style="left:18px;top:17px" width="13" height="10" viewBox="0 0 13 10"><rect width="13" height="10" rx="1" fill="#bbb"/></svg>
      <svg class="abs" style="left:226px;top:15px" width="16" height="16" viewBox="0 0 16 16"><path d="M1 7l14-6-6 14-2-6z" fill="#3fc89b"/></svg>
    </div>
  </div>
  <div class="to-top"><svg width="40" height="40" viewBox="0 0 40 40"><path d="M20 27V13M15 18l5-5 5 5" stroke="#222" stroke-width="1.6" fill="none"/></svg></div>
  <div class="copyright">© COPYRIGHT 2023, ALL BRINDEL ASSET DEVELOPMENT</div>
</footer>

</body>
</html>
```